VKT Logistics Marketing flyer

Good morning, I run a trucking company and I will be needing help setting up a website logo and a marketing flyer or something like that talking about our services and what we can offer to potential new customers who need to ship their product. I need help getting this all together.

Target Market(s)

Transportation customers

Requirements
Must have
• should list our services and contact info
Nice to have
• the Logo on the top

```html
<!DOCTYPE html>
<html lang="en">
<head>
<meta charset="utf-8">
<title>VKT Logistics Flyer</title>
<link href="https://fonts.googleapis.com/css2?family=Fira+Sans:wght@400;600;700&family=Inter:wght@400;600&display=swap" rel="stylesheet">
<style>
:root{
  --bg:#d3d4d6;
  --orange:#e8492a;
  --green:#1e6b35;
  --dark:#3f3f41;
  --grey:#5d5e60;
  --white:#ffffff;
  --ink:#2a2a2a;
}
*{margin:0;padding:0;box-sizing:border-box}
html,body{width:1200px;height:800px;overflow:hidden;background:var(--bg);font-family:"Inter",sans-serif}
.page{position:absolute;top:136px;width:408px;height:528px;background:var(--white);overflow:hidden;box-shadow:4px 4px 8px rgba(0,0,0,.35)}
.page--front{left:168px}
.page--back{left:624px}
.abs{position:absolute}
.shapes{position:absolute;left:0;top:0;width:408px;height:528px}
.brand{left:31px;top:34px;display:flex;align-items:center;gap:6px;font-family:"Fira Sans",sans-serif;font-weight:700;font-size:19px;color:var(--green)}
.brand__dot{width:14px;height:14px;border-radius:50%;background:var(--orange)}
.headline{left:21px;top:146px;font-family:"Fira Sans",sans-serif;font-weight:700;font-size:25px;line-height:29px;color:var(--white)}
.body-copy{font-size:6.8px;line-height:8.9px;color:var(--ink)}
.intro{left:15px;top:254px;width:160px}
.apart{left:196px;top:255px;width:192px;height:254px;background:var(--green);border-radius:12px;overflow:hidden}
.apart__title{height:30px;text-align:center;font-family:"Fira Sans",sans-serif;font-weight:700;font-size:15px;line-height:30px;color:var(--white);border-bottom:1.5px solid var(--white)}
.apart__grid{display:grid;grid-template-columns:1fr 1fr;grid-template-rows:101px 1fr;height:224px}
.apart__cell{display:flex;flex-direction:column;align-items:center;padding:12px 6px 0;color:var(--white);font-size:5.6px;line-height:8px;font-weight:600;text-align:center}
.apart__cell:nth-child(odd){border-right:1.5px solid var(--white)}
.apart__cell:nth-child(-n+2){border-bottom:1.5px solid var(--white)}
.apart__icon{width:48px;height:48px;border-radius:7px;background:var(--orange);margin-bottom:12px;display:flex;align-items:center;justify-content:center}
.back-text{left:10px;top:13px;width:222px}
.refs-title{left:17px;top:145px;font-family:"Fira Sans",sans-serif;font-weight:700;font-size:16.5px;color:var(--white)}
.refs{left:48px;top:195px;width:360px;height:46px;display:flex;align-items:center;justify-content:space-around;padding-right:10px;font-family:"Fira Sans",sans-serif;font-weight:600;font-size:12px;color:var(--white)}
.winner{left:5px;top:261px;display:flex;align-items:center;gap:6px;color:var(--white);font-family:"Fira Sans",sans-serif}
.winner__num{width:30px;height:32px;background:var(--white);color:var(--green);border-radius:6px;font-weight:700;font-size:27px;line-height:32px;text-align:center}
.winner__txt{font-size:11.5px;line-height:11px;font-weight:600}
.winner__txt span{letter-spacing:3px;font-weight:400}
.award{left:14px;top:313px;font-family:"Fira Sans",sans-serif}
.award__name{display:flex;align-items:center;gap:5px;font-weight:700;font-size:15px;color:var(--ink)}
.award__dot{width:16px;height:16px;border-radius:50%;background:#2a7fc9}
.award__sub{font-size:6px;color:var(--ink);margin-top:2px;letter-spacing:.3px}
.award__title{font-size:8.5px;font-weight:600;color:#2a7fc9;margin-top:3px}
.win-box{left:6px;top:371px;width:277px;height:103px;background:var(--green);border-radius:12px;padding:14px 14px;color:var(--white);font-size:6.6px;line-height:8.8px}
.footer{left:0;top:491px;width:408px;height:37px;background:var(--dark);color:var(--white);display:flex;align-items:center;gap:8px;padding:0 5px;font-size:6px}
.footer__brand{font-family:"Fira Sans",sans-serif;font-weight:600;font-size:8px;line-height:9px}
.footer__brand small{display:block;font-weight:400;font-size:6px;letter-spacing:.6px}
.footer__col{line-height:11px}
.footer__col b{font-size:8px}
.badge{background:var(--white);color:var(--dark);border-radius:4px;padding:0 2px;font-weight:700}
.footer__sep{width:1px;height:24px;background:#888}
.footer__circle{width:14px;height:14px;border-radius:50%;background:var(--white)}
</style>
</head>
<body>

<section class="page page--front">
  <svg class="shapes" viewBox="0 0 408 528">
    <path d="M0 123 H300 C325 170 360 200 408 210 V233 H0 Z" fill="var(--orange)"/>
    <line x1="10" y1="143" x2="176" y2="143" stroke="#fff" stroke-width="1"/>
    <line x1="10" y1="214" x2="243" y2="214" stroke="#fff" stroke-width="1"/>
    <path d="M164 0 C175 150 270 240 408 246" fill="none" stroke="var(--orange)" stroke-width="3"/>
    <path d="M171 0 C182 145 275 234 408 240" fill="none" stroke="var(--green)" stroke-width="3"/>
    <path d="M179 0 C190 140 280 230 408 234 V0 Z" fill="#8a7a6a" role="img" aria-label="Aerial photo of a truck hauling a container past stacked shipping containers"/>
    <rect x="0" y="429" width="189" height="99" fill="#7a8794" role="img" aria-label="Photo of a container port with cranes and trucks"/>
    <rect x="388" y="429" width="20" height="99" fill="#6d7885"/>
    <rect x="190" y="249" width="200" height="264" rx="14" fill="#fff" stroke="var(--orange)" stroke-width="2.5"/>
  </svg>

  <div class="abs brand"><span class="brand__dot"></span>VKT LOGISTICS</div>
  <h1 class="abs headline">Specialists in<br>Moving Products</h1>

  <p class="abs body-copy intro">VKT Logistics LLC is a transportation company that specializes in maximizing the efficiency in moving products from shipper to customer in the shortest, safest time possible. We have the knowledge and ability to handle any dry van, reefer, flatbed, or tanker load that needs to be moved. We strive to be your number one call to bring or move any product that your company may need. With our current 30 truck fleet, we can service customers locally to across country with solo and team drivers to make sure that your product is to your customers in the time frame promised. VKT can additionally adjust to each customer’s needs so if the need arises, we can add to the fleet to make sure that you, the customer, are getting the service that you need.</p>

  <div class="abs apart">
    <h2 class="apart__title">What sets us apart</h2>
    <div class="apart__grid">
      <div class="apart__cell">
        <div class="apart__icon"><svg width="28" height="28" viewBox="0 0 28 28" fill="none" stroke="#fff" stroke-width="2"><circle cx="14" cy="8" r="5"/><path d="M5 25 V19 H23 V25 Z M8 19 C8 15 20 15 20 19"/></svg></div>
        When you call you will get either the owner or the CFO
      </div>
      <div class="apart__cell">
        <div class="apart__icon"><svg width="28" height="28" viewBox="0 0 28 28" fill="none" stroke="#fff" stroke-width="2"><path d="M6 3 H18 M6 25 H14 M8 3 C8 10 16 10 16 14 C16 18 8 18 8 25"/><circle cx="20" cy="20" r="6" fill="#fff"/><path d="M20 17 V20 H22" stroke="var(--orange)"/></svg></div>
        You will not have to wait for approvals and time wasted.
      </div>
      <div class="apart__cell">
        <div class="apart__icon"><svg width="28" height="28" viewBox="0 0 28 28" fill="none" stroke="#fff" stroke-width="2"><circle cx="8" cy="7" r="4"/><path d="M8 12 V16 C8 20 18 16 18 21 C18 24 14 24 12 24"/><circle cx="22" cy="22" r="3" fill="#fff"/></svg></div>
        We work through the problems to find the right solution then get it executed quickly and effectively.
      </div>
      <div class="apart__cell">
        <div class="apart__icon"><svg width="28" height="28" viewBox="0 0 28 28" fill="none" stroke="#fff" stroke-width="2"><path d="M5 16 V13 A9 9 0 0 1 23 13 V16"/><rect x="3" y="15" width="4" height="6" rx="1"/><rect x="21" y="15" width="4" height="6" rx="1"/><path d="M14 22 L9 17 A2.5 2.5 0 0 1 14 14 A2.5 2.5 0 0 1 19 17 Z" fill="#fff"/></svg></div>
        You are not just another number to us you are what makes our company possible, and we value that relationship.
      </div>
    </div>
  </div>
</section>

<section class="page page--back">
  <svg class="shapes" viewBox="0 0 408 528">
    <path d="M0 121 H260 C290 160 330 180 408 182 V185 H36 V251 H0 Z" fill="var(--orange)"/>
    <line x1="7" y1="139" x2="262" y2="139" stroke="#fff" stroke-width="1"/>
    <line x1="7" y1="174" x2="292" y2="174" stroke="#fff" stroke-width="1"/>
    <path d="M222 0 C235 105 300 180 408 185" fill="none" stroke="var(--orange)" stroke-width="3"/>
    <path d="M230 0 C243 100 305 174 408 179" fill="none" stroke="var(--green)" stroke-width="3"/>
    <path d="M239 0 C252 95 310 168 408 172 V0 Z" fill="#9a7a55" role="img" aria-label="Photo of a warehouse worker checking inventory on a clipboard"/>
    <path d="M70 185 H408 V251 H70 A33 33 0 0 1 70 185 Z" fill="var(--dark)"/>
    <path d="M75 193 H408 V243 H75 A25 25 0 0 1 75 193 Z" fill="var(--grey)"/>
    <rect x="129" y="256" width="279" height="115" fill="#a69a7c" role="img" aria-label="Photo of a highway through open fields at sunset with trucks"/>
    <rect x="0" y="371" width="408" height="120" fill="#8b8f93" role="img" aria-label="Continuation of highway photo"/>
    <path d="M0 257 H100 A20 20 0 0 1 100 297 H0 Z" fill="var(--orange)"/>
    <path d="M0 255 H95 A20 20 0 0 1 95 295 H0 Z" fill="var(--green)"/>
    <rect x="3" y="367" width="284" height="110" rx="14" fill="#fff" stroke="var(--orange)" stroke-width="2"/>
  </svg>

  <p class="abs body-copy back-text">We take pride in our work and our customer service from pick up to delivery. Our current customer list handles more than half of the nation’s imported orange juice, hauling the corn oil that fries the potato chips for one of the nation’s largest potato chip suppliers, to hauling wine from the west coast doing plant to plant transfers to the plants on the east coast. We also branch out to haul the corn syrup in to make the wine and alcohol out of the plant in the Midwest to the different plants that make alcohol. In short, from a transportation standpoint if you need it, we can bring it to you rather it is the ingredient’s coming into your plant or your product leaving.</p>

  <h2 class="abs refs-title">Our references include those from</h2>
  <div class="abs refs"><span>Orchard Vale</span><span>Sunbrook</span><span>Crispfield</span><span>Northmark</span></div>

  <div class="abs winner"><div class="winner__num">2</div><div class="winner__txt"><span>Times</span><br>Winner</div></div>

  <div class="abs award">
    <div class="award__name">Summit Freight<span class="award__dot"></span></div>
    <div class="award__sub">SUMMIT FREIGHT BROKERS</div>
    <div class="award__title">Elite Carrier Award</div>
  </div>

  <p class="abs win-box">To date, we have won the Summit Freight Elite Carrier Excellence Award two years in a row servicing their major customers across their different brokerage networks. VKT is the number one truck supplier to two of the major orange juice manufacturers in the US for when they bring their product into port side in Florida, and it needs to go to their manufacturing facility throughout the state. In the past year, we have hauled over 40 million gallons of orange juice, another million gallons of wine and alcohol and millions of gallons of corn oil to service the nation’s food industry with the ability to add to that ever-growing number.</p>

  <footer class="abs footer">
    <span class="footer__circle"></span>
    <div class="footer__brand">VKT Logistics LLC<small>Established in 2010</small></div>
    <div class="footer__sep"></div>
    <div class="footer__col">⌖ 418 Birch Ln. Marlow, IN. 47001<br>✉ vktlogisticsllc@mail.com</div>
    <div class="footer__sep"></div>
    <div class="footer__col"><span class="badge">CFO</span> Dana Whitfield<br><b>✆ 555-014-2270</b></div>
    <div class="footer__col"><span class="badge">CEO</span> Marcus Hale<br><b>✆ 555-014-8836</b></div>
  </footer>
</section>

</body>
</html>
```